Reliable and clean label for a natural product!

We would like to have a label design for our CBD SOFT GEL CAPSULES . We are a business family and believe in the power of natural healing. In this label we would like to show a reliable, natural and feminine product mainly.

Font styles to use
Serif
Sans Serif

Colors

Designer to choose colors to be used in the design.

```html
<!DOCTYPE html>
<html lang="en">
<head>
<meta charset="utf-8">
<title>Verdalia CBD – Capsule Label</title>
<link href="https://fonts.googleapis.com/css2?family=Montserrat:wght@400;500;600;700&display=swap" rel="stylesheet">
<style>
  :root {
    --page-bg: #eef2f3;
    --label-white: #ffffff;
    --brand-blue: #2b98d4;
    --band-purple: #7a5ba6;
    --panel-teal: #28a796;
    --count-blue: #3b9fd6;
    --text-light: #f4f1f8;
  }
  * { margin: 0; padding: 0; box-sizing: border-box; }
  html, body {
    width: 1200px; height: 1200px; overflow: hidden;
    background: var(--page-bg);
    font-family: "Montserrat", sans-serif;
  }
  .canvas {
    width: 1200px; height: 1200px;
    display: flex; align-items: center; justify-content: center;
  }
  .label {
    width: 800px; height: 976px;
    display: flex; flex-direction: column;
    box-shadow: 0 10px 40px rgba(40, 60, 90, 0.12);
  }
  .brand-zone {
    height: 274px; background: var(--label-white);
    display: flex; flex-direction: column; align-items: center;
    padding-top: 50px;
  }
  .brand-mark { width: 134px; height: 134px; }
  .brand-name {
    margin-top: 16px;
    font-size: 56px; font-weight: 500; letter-spacing: 1px;
    color: var(--brand-blue); line-height: 1;
  }
  .product-zone {
    height: 612px; background: var(--band-purple);
    display: flex; flex-direction: column; align-items: center;
    color: var(--text-light);
  }
  .product-kicker {
    margin-top: 32px;
    font-size: 34px; font-weight: 600; letter-spacing: 0.5px; line-height: 1;
  }
  .product-title {
    margin-top: 28px;
    width: 532px; height: 318px;
    background: var(--panel-teal);
    display: flex; flex-direction: column; justify-content: center; align-items: center;
    font-size: 84px; font-weight: 700; line-height: 1.2; letter-spacing: 1px;
    text-align: center;
  }
  .product-subtitle {
    margin-top: 28px;
    font-size: 38px; font-weight: 500; line-height: 1;
  }
  .product-specs {
    margin-top: 34px;
    font-size: 33px; font-weight: 400; line-height: 1.3; text-align: center;
  }
  .count-band {
    height: 90px; background: var(--count-blue);
    display: flex; align-items: center; justify-content: center;
    color: var(--text-light);
    font-size: 34px; font-weight: 500; letter-spacing: 1px;
  }
</style>
</head>
<body>
  <main class="canvas">
    <section class="label">
      <header class="brand-zone">
        <svg class="brand-mark" viewBox="0 0 134 134" aria-hidden="true">
          <circle cx="67" cy="67" r="63" fill="none" stroke="#2b98d4" stroke-width="4"/>
        </svg>
        <div class="brand-name">VERDALIA CBD</div>
      </header>
      <div class="product-zone">
        <p class="product-kicker">RESTORATIVE SUPPLEMENT</p>
        <h1 class="product-title">
          <span>CAPSULAS</span>
          <span>ACEITE DE</span>
          <span>CBD</span>
        </h1>
        <p class="product-subtitle">Hemp Oil Extract Capsules</p>
        <p class="product-specs">Full Spectrum<br>25 mg CBD per capsule</p>
      </div>
      <footer class="count-band">30 CAPSULES</footer>
    </section>
  </main>
</body>
</html>
```